Sleek and elegant promotional banner/sign for The Vellinor Law Firm

We need a design for promotional items like banners, signs, print ads, etc. that includes our firm name - "The Vellinor Law Firm" - and what we do. We advise businesses and individuals on legal matters; we represent individuals and businesses in litigation and transactions; we select and create business entities; we solve legal problems for individuals and businesses, etc. PLEASE DO NOT SIMPLY REPEAT THE PREVIOUS SENTENCE ON THE DESIGN. Please create a tag-line or brief description from ours. We need something that describes what we do in concise and creative manner while communicating trust and confidence. The banner must also include our basic contact information: 948.512-7740 (telephone) and vellinorlaw.com (website). You may use one or more of the attached images, but needn't use any with the right design. The design should be sleek and modern.

Target Market(s)

wealthy individuals and small business owners, entrepreneurs

Industry/Entity Type

Lawyer

Font styles to use
Sans Serif

Colors
33a6d7
0556a4
33b8a4

Requirements
Must have
• Firm name, contact information, BRIEF description of our services, sleek and elegant.
• Also, the design must be horizontal - not vertical.
Nice to have
• I'd like to use one of the images
Should not have
• Cliches

```html
<!DOCTYPE html>
<html lang="en">
<head>
<meta charset="utf-8">
<title>The Vellinor Law Firm — Banner</title>
<link rel="stylesheet" href="https://fonts.googleapis.com/css2?family=Libre+Baskerville&family=Roboto:wght@300;400;700&display=swap">
<style>
  :root {
    --ink: #1f1f1f;
    --bronze: #8c6a44;
    --bar: #1b1b1b;
    --white: #ffffff;
    --sky-light: #f4f5f6;
    --sky-mid: #d9dcdf;
    --sky-dark: #b9bdc1;
  }
  html, body {
    margin: 0;
    padding: 0;
    overflow: hidden;
    background: var(--white);
  }
  .banner {
    position: relative;
    width: 1200px;
    height: 720px;
    overflow: hidden;
    font-family: "Roboto", "Helvetica Neue", Arial, sans-serif;
    color: var(--ink);
  }
  .backdrop {
    position: absolute;
    inset: 0;
    background:
      radial-gradient(ellipse at 30% 55%, rgba(255,255,255,0.9) 0%, rgba(255,255,255,0) 60%),
      linear-gradient(160deg, var(--sky-mid) 0%, var(--sky-light) 40%, var(--sky-light) 60%, var(--sky-dark) 100%);
  }
  .veil {
    position: absolute;
    inset: 0;
    background: rgba(255,255,255,0.55);
  }
  .firm {
    position: absolute;
    top: 72px;
    left: 0;
    right: 0;
    display: flex;
    justify-content: center;
    align-items: center;
    gap: 26px;
  }
  .firm-square {
    width: 58px;
    height: 58px;
    background: var(--ink);
  }
  .firm-name {
    font-family: "Libre Baskerville", "Times New Roman", serif;
    font-size: 31px;
    letter-spacing: 1px;
    text-transform: uppercase;
    color: var(--ink);
  }
  .headline {
    position: absolute;
    top: 198px;
    left: 0;
    right: 0;
    margin: 0;
    text-align: center;
    font-weight: 300;
    font-size: 84px;
    line-height: 98px;
  }
  .headline .lead { display: block; color: var(--ink); }
  .headline .accent { display: block; color: var(--bronze); }
  .services {
    position: absolute;
    top: 436px;
    left: 130px;
    right: 130px;
    margin: 0;
    text-align: center;
    font-size: 26px;
    line-height: 38px;
    font-weight: 400;
    color: var(--ink);
  }
  .contact-bar {
    position: absolute;
    left: 0;
    right: 0;
    bottom: 0;
    height: 90px;
    background: var(--bar);
    display: flex;
    justify-content: center;
    align-items: center;
    color: var(--white);
  }
  .phone {
    font-weight: 700;
    font-size: 46px;
    letter-spacing: 0.5px;
  }
  .divider {
    width: 2px;
    height: 52px;
    background: var(--white);
    margin: 0 38px 0 42px;
  }
  .website {
    font-weight: 400;
    font-size: 44px;
  }
</style>
</head>
<body>
  <div class="banner">
    <div class="backdrop" role="img" aria-label="Soft grey photograph looking up at a glass office tower against the sky"></div>
    <div class="veil"></div>

    <div class="firm">
      <div class="firm-square"></div>
      <div class="firm-name">The Vellinor Law Firm</div>
    </div>

    <h1 class="headline">
      <span class="lead">Committed to</span>
      <span class="accent">Helping Our Clients Succeed</span>
    </h1>

    <p class="services">We provides exceptional results for our clients, and has experience in cases involving business, contracts, real estate, shareholder and partnership disputes, and estate planning.</p>

    <div class="contact-bar">
      <span class="phone">948.512-7740</span>
      <span class="divider"></span>
      <span class="website">vellinorlaw.com</span>
    </div>
  </div>
</body>
</html>
```